The Quiet Lantern - The best guide in your pocket

The Quiet Lantern (فانوس‌آرام in Persian)

We need a new app design for a major update on Android, iOS and Windows Universal platforms.
Our company works on creating innovative apps and games on different platforms, this particular app is free for end users and provides location based services. Here is the abstract feature list:
• Nearest points around user (explore on map or find) including locations, events and skills
• Add points to our database (partners) plus comments and ratings
• Point owners can modify or complete their points data, provide sale events, services and …

Attachments:
Our service logo
The detailed descriptions of different sections (PDF documents)
Updates

Project Deadline Extended Reason: We want more designs :)Give us previews on Home and Map sections at least (more interesting if previews are provided for more sections) Added Saturday, January 7, 2017

Target Market(s)

Public

Industry/Entity Type

Android

Font styles to use
Serif
Sans Serif

Requirements
Must have
• Consider attached service logo & wireframe
• Designs for attached sections
• Fluent user experience
• Modern design
Nice to have
• Right to Left layouts
Should not have
• No alphabet in graphic assets

```html
<!DOCTYPE html>
<html lang="en">
<head>
<meta charset="utf-8">
<title>The Quiet Lantern – Create Account</title>
<link rel="stylesheet" href="https://fonts.googleapis.com/css2?family=Montserrat:wght@400;500;600;700&family=Vazirmatn:wght@700&display=swap">
<style>
  :root {
    --canvas-bg: #eceef1;
    --screen-bg: #ffffff;
    --sky-teal: #7ac8c1;
    --sky-warm: #a9c9a0;
    --slate: #41606f;
    --heading: #3e5a6a;
    --muted: #808b91;
    --accent-teal: #6cc4bc;
    --field-bg: #f4f5f7;
    --placeholder: #a9b1b6;
    --social: #4862a3;
    --social-dark: #3e5593;
    --ink: #111111;
    --white: #ffffff;
  }
  * { box-sizing: border-box; margin: 0; padding: 0; }
  html, body {
    width: 1000px; height: 1200px; overflow: hidden;
    background: var(--canvas-bg);
    font-family: "Montserrat", sans-serif;
  }
  .screen {
    position: absolute; left: 162px; top: 0;
    width: 676px; height: 1200px;
    background: var(--screen-bg);
    overflow: hidden;
  }
  .hero {
    position: absolute; left: 0; top: 0; width: 676px; height: 320px;
  }
  .hero-art {
    position: absolute; left: 0; top: 0; width: 676px; height: 320px;
    background: linear-gradient(180deg, var(--sky-teal) 0%, var(--sky-teal) 60%, var(--sky-warm) 100%);
  }
  .status-bar {
    position: absolute; left: 0; top: 0; width: 676px; height: 48px;
    display: flex; align-items: center; justify-content: space-between;
    padding: 0 14px 0 16px;
    font-size: 19px; font-weight: 500; color: var(--ink);
  }
  .status-left, .status-right { display: flex; align-items: center; gap: 6px; width: 200px; }
  .status-right { justify-content: flex-end; }
  .status-time { font-weight: 600; }
  .battery { width: 38px; height: 16px; background: var(--ink); border-radius: 3px; position: relative; }
  .battery::after { content: ""; position: absolute; right: -4px; top: 5px; width: 3px; height: 6px; background: var(--ink); border-radius: 0 2px 2px 0; }
  .brand {
    position: absolute; left: 0; top: 330px; width: 676px; height: 96px;
    display: flex; align-items: center; justify-content: center; gap: 18px;
  }
  .brand-mark { width: 58px; height: 58px; border-radius: 50%; background: var(--slate); }
  .brand-name {
    font-family: "Vazirmatn", sans-serif; font-weight: 700;
    font-size: 62px; color: var(--slate); line-height: 1;
  }
  .title {
    position: absolute; left: 0; top: 460px; width: 676px; text-align: center;
    font-size: 43px; font-weight: 500; color: var(--heading);
  }
  .subtitle {
    position: absolute; left: 0; top: 522px; width: 676px; text-align: center;
    font-size: 24px; font-weight: 500; color: var(--muted);
  }
  .subtitle a { color: var(--accent-teal); font-weight: 600; text-decoration: none; }
  .field {
    position: absolute; left: 110px; width: 452px; height: 90px;
    background: var(--field-bg);
    display: flex; align-items: center; justify-content: center;
    font-size: 25px; color: var(--placeholder); letter-spacing: .5px;
  }
  .field-name { top: 586px; }
  .field-email { top: 703px; }
  .field-password { top: 820px; }
  .btn-register {
    position: absolute; left: 110px; top: 936px; width: 449px; height: 82px;
    background: var(--slate); color: var(--white);
    display: flex; align-items: center; justify-content: center;
    font-size: 26px; font-weight: 700; letter-spacing: 1px;
  }
  .btn-social {
    position: absolute; left: 110px; top: 1052px; width: 449px; height: 80px;
    background: var(--social); color: var(--white); display: flex;
  }
  .btn-social-icon {
    width: 80px; height: 80px; background: var(--social-dark);
    display: flex; align-items: center; justify-content: center;
  }
  .btn-social-icon span { width: 22px; height: 22px; background: var(--white); }
  .btn-social-label {
    flex: 1; display: flex; align-items: center; justify-content: center;
    font-size: 22px; font-weight: 500; letter-spacing: .5px;
  }
  .btn-social-label b { font-weight: 700; margin-left: 6px; }
</style>
</head>
<body>
  <main class="screen">
    <div class="hero">
      <div class="hero-art" role="img" aria-label="Illustration of looping roads with a bus and a ship travelling over them, rising above white clouds"></div>
      <div class="status-bar">
        <div class="status-left">
          <svg width="58" height="12" viewBox="0 0 58 12" aria-hidden="true">
            <circle cx="6" cy="6" r="5" fill="#111"/><circle cx="18" cy="6" r="5" fill="#111"/><circle cx="30" cy="6" r="5" fill="#111"/>
            <circle cx="42" cy="6" r="4.3" fill="none" stroke="#111" stroke-width="1.2"/><circle cx="53" cy="6" r="4.3" fill="none" stroke="#111" stroke-width="1.2"/>
          </svg>
          <span>ORBIT</span>
          <svg width="20" height="16" viewBox="0 0 20 16" aria-hidden="true">
            <path d="M10 15 L6.5 11 A5 5 0 0 1 13.5 11 Z" fill="#111"/>
            <path d="M3.5 8 A9 9 0 0 1 16.5 8" fill="none" stroke="#111" stroke-width="2"/>
            <path d="M0.8 5 A13 13 0 0 1 19.2 5" fill="none" stroke="#111" stroke-width="2"/>
          </svg>
        </div>
        <span class="status-time">4:21 PM</span>
        <div class="status-right">
          <svg width="12" height="18" viewBox="0 0 12 18" aria-hidden="true">
            <path d="M2 5 L10 13 L6 17 L6 1 L10 5 L2 13" fill="none" stroke="#555" stroke-width="1.4"/>
          </svg>
          <span>100%</span>
          <span class="battery"></span>
        </div>
      </div>
    </div>

    <div class="brand">
      <span class="brand-name" lang="fa" dir="rtl">فانوس‌آرام</span>
      <span class="brand-mark" aria-hidden="true"></span>
    </div>

    <h1 class="title">Create Account</h1>
    <p class="subtitle">Already have an account? <a href="#">Sign in</a></p>

    <div class="field field-name">Name</div>
    <div class="field field-email">E-mail</div>
    <div class="field field-password">Password</div>

    <div class="btn-register">REGISTER</div>

    <div class="btn-social">
      <div class="btn-social-icon"><span></span></div>
      <div class="btn-social-label">Connect with <b>Linkfolk</b></div>
    </div>
  </main>
</body>
</html>
```